New business card design for Maplewood Ridge Optometry Clinic

We need a new business card design using our existing logo (uploaded). Please do not include eyes, eye exam charts or beaches, water, sand. The logo I uploaded shows our colors of green and blue, but we are open to seeing it in black OR white. We would like to see something modern and fresh. It will need to be 2 sided. On the front we will need to be able to put a doctors name, for example-Dr Clara Venhuisen and Associates. We will need to be able to change the name to other doctors names when we send for printing. The back of the card should list the following: 1748 Tarrow St, Elmstead Harbour (P)555-555-0183 (E) info@mroc-example.ca www.mroc-example.ca. "We are welcoming new patients" and a line for the appointment date and time. I have uploaded the back of a card to give an example

```html
<!DOCTYPE html>
<html lang="en">
<head>
<meta charset="utf-8">
<title>Maplewood Ridge Optometry Clinic – Business Card</title>
<link href="https://fonts.googleapis.com/css2?family=Montserrat:wght@700;800&family=Open+Sans:wght@400;800&display=swap" rel="stylesheet">
<style>
  :root {
    --bg: #2b2a2a;
    --card-dark: #2f2f30;
    --card-light: #ffffff;
    --brand-blue: #4a63b5;
    --brand-blue-shade: #34488a;
    --brand-green: #2e9e55;
    --ink: #333333;
    --dots: #555555;
  }
  * { margin: 0; padding: 0; box-sizing: border-box; }
  html, body { width: 1200px; height: 939px; overflow: hidden; }
  body {
    background: var(--bg);
    font-family: "Open Sans", sans-serif;
    position: relative;
  }
  .card {
    position: absolute;
    width: 540px;
    height: 310px;
    border-radius: 18px;
    box-shadow: 0 14px 30px rgba(0,0,0,.45);
    overflow: hidden;
  }
  .card-front {
    left: 40px; top: 314px;
    background: var(--card-dark);
    display: flex; flex-direction: column; align-items: center; justify-content: center;
    text-align: center;
  }
  .brand-name {
    display: flex; align-items: center; gap: 14px;
    font-family: "Montserrat", sans-serif;
    font-weight: 800;
    color: var(--brand-blue);
    font-size: 30px;
    line-height: 1.15;
    text-align: left;
  }
  .brand-dot {
    width: 46px; height: 46px; border-radius: 50%;
    background: var(--brand-green);
    flex: none;
  }
  .doctor-name {
    margin-top: 40px;
    font-family: "Montserrat", sans-serif;
    font-weight: 700;
    color: var(--brand-blue);
    font-size: 19px;
    letter-spacing: .5px;
  }
  .card-back {
    left: 620px; top: 314px;
    background: var(--card-light);
    padding: 34px 34px 26px;
  }
  .back-top { display: flex; align-items: center; gap: 36px; padding-left: 46px; }
  .back-mark {
    width: 88px; height: 88px; border-radius: 50%;
    background: var(--brand-blue);
    flex: none;
  }
  .contact-list { list-style: none; color: var(--ink); font-size: 15px; line-height: 1.4; text-transform: uppercase; }
  .contact-list li { display: flex; align-items: flex-start; gap: 10px; }
  .contact-list svg { width: 13px; height: 13px; margin-top: 4px; flex: none; fill: var(--brand-green); }
  .banner {
    margin: 22px 0 0;
    background: var(--brand-blue);
    color: #fff;
    font-weight: 800;
    font-size: 21px;
    border-radius: 24px;
    padding: 7px 20px;
    text-align: center;
    box-shadow: 0 3px 0 var(--brand-blue-shade);
  }
  .appt { margin-top: 20px; display: flex; flex-direction: column; gap: 18px; }
  .appt-row { display: flex; align-items: baseline; gap: 4px; font-size: 13px; color: var(--brand-green); text-transform: uppercase; }
  .fill { flex: 1; border-bottom: 2px dotted var(--dots); height: 1px; }
</style>
</head>
<body>
  <section class="card card-front" aria-label="Card front">
    <div class="brand-name">
      <span class="brand-dot"></span>
      <span>Maplewood Ridge<br>Optometry Clinic</span>
    </div>
    <p class="doctor-name">Dr. Clara Venhuisen &amp; Associates.</p>
  </section>

  <section class="card card-back" aria-label="Card back">
    <div class="back-top">
      <span class="back-mark"></span>
      <ul class="contact-list">
        <li>
          <svg viewBox="0 0 24 24"><path d="M12 2a7 7 0 0 0-7 7c0 5 7 13 7 13s7-8 7-13a7 7 0 0 0-7-7zm0 9.5A2.5 2.5 0 1 1 12 6.5a2.5 2.5 0 0 1 0 5z"/></svg>
          <span>1748 Tarrow St<br>Elmstead Harbour</span>
        </li>
        <li>
          <svg viewBox="0 0 24 24"><path d="M6.6 10.8a15 15 0 0 0 6.6 6.6l2.2-2.2a1 1 0 0 1 1-.25 11.4 11.4 0 0 0 3.6.57 1 1 0 0 1 1 1V20a1 1 0 0 1-1 1A17 17 0 0 1 3 4a1 1 0 0 1 1-1h3.5a1 1 0 0 1 1 1c0 1.25.2 2.45.57 3.6a1 1 0 0 1-.25 1z"/></svg>
          <span>555-555-0183</span>
        </li>
        <li>
          <svg viewBox="0 0 24 24"><path d="M2 5h20v14H2zm2 2v.5l8 5 8-5V7zm0 2.8V17h16V9.8l-8 5z"/></svg>
          <span>info@mroc-example.ca</span>
        </li>
        <li>
          <svg viewBox="0 0 24 24"><path d="M12 2a10 10 0 1 0 0 20 10 10 0 0 0 0-20zm0 2a8 8 0 0 1 7.75 6H16a13 13 0 0 0-1.5-5.6A8 8 0 0 1 12 4zm-3 1a13 13 0 0 0-1 5H4.25A8 8 0 0 1 9 5zm-4.75 7H8a13 13 0 0 0 1 5 8 8 0 0 1-4.75-5zm7.75 8a8 8 0 0 1-1-.1A11 11 0 0 1 10 12h4a11 11 0 0 1-1 7.9 8 8 0 0 1-1 .1zm3-1a13 13 0 0 0 1-5h3.75A8 8 0 0 1 15 19z"/></svg>
          <span>mroc-example.ca</span>
        </li>
      </ul>
    </div>
    <p class="banner">WE ARE WELCOMING NEW PATIENTS!</p>
    <div class="appt">
      <div class="appt-row"><span>Doctor:</span><span class="fill"></span></div>
      <div class="appt-row"><span>Date:</span><span class="fill"></span><span>Time:</span><span class="fill"></span><span>AM/PM</span></div>
    </div>
  </section>
</body>
</html>
```